MODERN + COOL Business Card Needed!

SUMMARY
This is for a 40+ year old family business that is transitioning to the 2nd generation and is in real need of a more modern facelift. Ive attached a company logo (I made quickly as an idea with my limited PSD skills) to start off with that you are welcome to change and draw ideas from. Ive also attached some screen shots of cards I like to give you an idea of my preferences.

WHAT WE DO
The company name is Kin Dart HK Ltd. But I prefer to just call it Kin Dart or Kin Dart with Hong Kong as kind of a sub heading on the business card. We own a factory as well as help our customers find factories to make their product. Product I mean, toys 99.9% of the time. Simple old school toys like board games, puzzles, wooden toys, baby/infant toys.

You can say we are a "sourcing" or "trading" or "consulting" company with a factory to help you do it. But since we deal with toys, i like to keep it modern and cool and fun, not serious like managing hedge funds.

WHAT WE ARE LOOKING FOR
A cool, unique looking business card that stands out. In terms of design, something modern and professional. I like darker colored cards and I like colors such as blue/green/dark gray, but am open to other colored themes. I Like bright lime green with gray, always though thats a nice combo. I prefer cards that are all colored and not so much white showing (I think). Ive attached a few screenshots of cards so take a look to get a feel of what I like.

We do alot of wooden stacking games in variety of colors too like Pulto, Roni, Torvanets (google these to check them out). So designs that sort of resemble stacking or building would be cool but totally not necessary.

In terms of the physical aspects of the card, Im looking for a card a bit different than the standard rectangular shape. Double sided. Little things like having corner(s) be round or different angle instead of square edge I always thought was nice. Its got to be mostly a normal card size, no folding or smaller cards that fit weird in your wallet. No vertical designs. Am open to VERY different/creative shapes (as long as it still fits in a wallet good like a normal buisness card.

Hi everyone!

Just wanted to write a message to everyone to let them know all submissions are being reviewed or have been reviewed.  If I have not responded with feedback, rest assure your submission was definitely looked at in detail but I either have just been too busy to respond (alot of submissions!), or its on my to be considered list.

I respect and really enjoy receiving everyones creativity and work so I dont want it to go unrecognized - thus this message!  Feel free to submit more ideas if you like until this project ends.  Sometimes some designs just dont click but sometimes they can so you never know!

Thanks again for everyones participation and great work!

~Dov Ruel

Target Market(s)

The cards are mainly handed to toy company sourcers and buyers. People I talk to ... say Quelvin for example... might want to make their next edition of Farthundle game with a reputable factory at a good cost so they can sell it to stores at a profit.

So these are the types of people I often try to talk and introduce myself and my company to.

Industry/Entity Type

Building

Colors
acd036
0392cd
00a88e
474747
606060

Requirements
Must have
• Just double sided, not plain rectangle corners, and just cool to look at and catches your eye!

Oh and the obvious business card stuff like place for name, address, number, email, etc.
Nice to have
• Think more modern and fun, not serious and old fashion (thats what we used to be!). Can use the logo I attached and you can definitely alter and change the logo or make a whole new one!

Oh and can definitely use a creative slogan if you like to think of one based on what I described in what we do.
Should not have
• Dont use fonts or text placement that might make "Kin Dart" look like "Kind Art"... We arent selling news papers!!

Please nothing related to education since we have the word Dart in the title, thats not our business at all.

Logo and design should not be too heavy on things related to toys, as though thats what we primarily focus on now, what we do may change over time.

```html
<!DOCTYPE html>
<html lang="en">
<head>
<meta charset="utf-8">
<title>Kin Dart Hong Kong – Business Card</title>
<link rel="stylesheet" href="https://fonts.googleapis.com/css2?family=Montserrat:wght@200;300;400;700&display=swap">
<style>
  :root {
    --lime: #acd036;
    --blue: #0392cd;
    --teal: #00a88e;
    --graphite: #474747;
    --slate: #606060;
    --backdrop: #e9e7e3;
    --ink-light: #e4e4e4;
    --ink-soft: #c9c9c9;
  }
  * { margin: 0; padding: 0; box-sizing: border-box; }
  html, body {
    width: 1200px; height: 750px; overflow: hidden;
    background: var(--backdrop);
    font-family: "Montserrat", sans-serif;
  }
  .stage { position: relative; width: 1200px; height: 750px; }
  .card {
    position: absolute; top: 225px; width: 520px; height: 300px;
    filter: drop-shadow(0 10px 18px rgba(0,0,0,.22));
  }
  .card--front { left: 50px; }
  .card--back { left: 630px; }
  .card__face { position: absolute; inset: 0; }
  .card--front .card__face {
    clip-path: polygon(44px 0, 100% 0, 100% 236px, 456px 100%, 0 100%, 0 44px);
  }
  .card--back .card__face {
    clip-path: polygon(0 0, 476px 0, 100% 44px, 100% 100%, 56px 100%, 0 244px);
  }
  .card__art { position: absolute; inset: 0; width: 520px; height: 300px; }

  .brand {
    position: absolute; left: 120px; top: 62px; width: 340px;
    display: flex; flex-direction: column; align-items: center;
    color: var(--lime); text-transform: uppercase; line-height: 1.05;
  }
  .brand__mark {
    width: 64px; height: 64px; border-radius: 50%;
    background: var(--lime); margin-bottom: 14px;
  }
  .brand__name { font-size: 42px; font-weight: 700; letter-spacing: 1px; }
  .brand__place { font-size: 26px; font-weight: 400; letter-spacing: 3px; margin-top: 4px; }

  .holder {
    position: absolute; right: 40px; top: 30px; text-align: right;
    color: var(--ink-light);
  }
  .holder__name { font-size: 32px; font-weight: 200; letter-spacing: .5px; }
  .holder__role { font-size: 12px; font-weight: 300; letter-spacing: 2px; margin-top: 2px; }

  .contact {
    position: absolute; left: 130px; top: 112px;
    display: grid; grid-template-columns: 18px 1px auto;
    grid-auto-rows: 24px; column-gap: 12px; align-items: center;
    color: var(--ink-soft); font-size: 13px; font-weight: 300;
  }
  .contact__icon { width: 16px; height: 16px; fill: var(--ink-light); grid-column: 1; }
  .contact__rule { grid-column: 2; grid-row: 1 / span 3; align-self: stretch; background: var(--ink-light); }
  .contact__line { grid-column: 3; }
</style>
</head>
<body>
<main class="stage">

  <section class="card card--front" aria-label="Card front">
    <div class="card__face">
      <svg class="card__art" viewBox="0 0 520 300" aria-hidden="true">
        <rect width="520" height="300" fill="var(--lime)"/>
        <polygon points="92,0 520,0 520,300 390,300 0,158 0,64" fill="var(--slate)"/>
        <polygon points="70,0 92,0 0,64 0,48" fill="var(--teal)" opacity=".55"/>
      </svg>
      <div class="brand">
        <div class="brand__mark"></div>
        <div class="brand__name">Kin Dart</div>
        <div class="brand__place">Hong Kong</div>
      </div>
    </div>
  </section>

  <section class="card card--back" aria-label="Card back">
    <div class="card__face">
      <svg class="card__art" viewBox="0 0 520 300" aria-hidden="true">
        <rect width="520" height="300" fill="var(--slate)"/>
        <polygon points="0,212 300,250 330,266 520,226 520,300 0,300" fill="var(--blue)"/>
        <polygon points="0,248 300,262 330,280 520,240 520,254 330,294 300,276 0,264" fill="var(--graphite)"/>
        <polygon points="450,0 476,0 520,44 520,74" fill="var(--teal)" opacity=".5"/>
      </svg>
      <div class="holder">
        <div class="holder__name">Lena Varsk</div>
        <div class="holder__role">DESIGNER</div>
      </div>
      <div class="contact">
        <svg class="contact__icon" style="grid-row:1" viewBox="0 0 16 16" aria-label="Phone"><path d="M4 1h8a1 1 0 0 1 1 1v12a1 1 0 0 1-1 1H4a1 1 0 0 1-1-1V2a1 1 0 0 1 1-1zm1 2v7h6V3zm3 9a1 1 0 1 0 0 2 1 1 0 0 0 0-2z"/></svg>
        <svg class="contact__icon" style="grid-row:2" viewBox="0 0 16 16" aria-label="Email"><path d="M1 3h14v10H1zm1.5 1.2L8 8.6l5.5-4.4zM2 5.4V12h12V5.4L8 10z"/></svg>
        <svg class="contact__icon" style="grid-row:3" viewBox="0 0 16 16" aria-label="Web"><path d="M8 1a7 7 0 1 0 0 14A7 7 0 0 0 8 1zm0 1.3c.8.9 1.4 2.3 1.6 4H6.4C6.6 4.6 7.2 3.2 8 2.3zM2.3 7.3h3c.1 1.6.5 3 1.1 4.1a5.7 5.7 0 0 1-4.1-4.1zm0-1A5.7 5.7 0 0 1 6.4 3.3C5.8 4 5.4 5.1 5.3 6.3zm4.1 1h3.2c-.2 1.7-.8 3.1-1.6 4-.8-.9-1.4-2.3-1.6-4zm4.2 0h3.1a5.7 5.7 0 0 1-4.1 4.1c.6-1.1 1-2.5 1-4.1zm3.1-1h-3.1c-.1-1.2-.5-2.3-1.1-3a5.7 5.7 0 0 1 4.2 3z"/></svg>
        <div class="contact__rule"></div>
        <span class="contact__line" style="grid-row:1">+ 852 3104 7720</span>
        <span class="contact__line" style="grid-row:2">info@kindart.com</span>
        <span class="contact__line" style="grid-row:3">www.kindart.com</span>
      </div>
    </div>
  </section>

</main>
</body>
</html>
```